Yukon Canada First Nation Website

I'm looking for a home page design that applies the navigation scheme of the included sitemap and show a proposed menu style for the website of a First Nation based in Yukon, Canada. The idea of incorporating Kaska language words into the site could be explored through the design; this links to several Kaska words and phrases http://www.nativetongueshub.org/en/Tessaly-Kaska/word-categories. Of the provided assets, the art in the archive file should just be used as a reference.
Updates

Want to provide more time for designers to respond and to create their concept submissions.

Slow in providing feedback

Target Market(s)

1. Tessaly First Nation members that the Tessaly First Nation government serves 2. Community Partners / Other Governments i.e. schools, community college, TVPS, municipality, territorial government 3. Business / Industry leaders who want to do business with the FIrst Nation or on their land.

Industry/Entity Type

Government

Font styles to use
Serif
Sans Serif
Other font styles liked:
• Vollkorn, Rosario, Roboto Slab, Ubuntu, Lato

Colors
0355a3
ec1f27
a54499
e24097
9bcb3c
fbee3d
33a6d7
85cae6
6b449b

Requirements
Must have
• - The Tessaly First Nation logo
• - Homepage Navigation sections: About Us, Government, Programs, Arms-length Entities, I want to
• - Elements of First Nations culture: language, colours/craft/art, clan symbols, nature, spirituality, care for land/elders
• - Professional, yet friendly and welcoming feel
Nice to have
• Spotlight image / slider on homepage
• People in the forefront
• Traditional colours often centre around the medicine wheel colours: primary red, yellow, black and white ... The colours indicated below are an analysis of the colours in Kaska art and are very colourful, inspired by nature. Those colours are not mandatory, but ideally the design is professional, polished and upbeat which can be established through colour use.

```html
<!DOCTYPE html>
<html lang="en">
<head>
<meta charset="utf-8">
<title>Tessaly First Nation – Home</title>
<link href="https://fonts.googleapis.com/css2?family=Vollkorn:ital,wght@0,400;0,600;0,700;1,400;1,600&family=Lato:wght@400;700&family=Raleway:wght@400;500;600&display=swap" rel="stylesheet">
<style>
:root{
  --red:#c4121b;
  --red-dark:#9e0d13;
  --orange:#f5a623;
  --gold:#f2b233;
  --ink:#222;
  --text:#555;
  --muted:#9a9a9a;
  --grey-bg:#ececec;
  --line:#dcdcdc;
  --dark:#2b2b2b;
  --wood:#7b2c12;
  --wood-light:#a2451f;
  --white:#fff;
}
*{box-sizing:border-box;margin:0;padding:0}
html,body{width:1200px;height:3666px;overflow:hidden}
body{position:relative;font-family:"Lato",sans-serif;color:var(--text);background:var(--white)}
.abs{position:absolute}
a{color:inherit;text-decoration:none}

/* top bar */
.topbar{left:0;top:0;width:1200px;height:44px;background:var(--red);color:#fff;font-size:12px;display:flex;align-items:center;padding:0 98px 0 122px;gap:30px}
.topbar .right{margin-left:auto;display:flex;align-items:center;gap:20px;font-weight:700;font-size:11px;letter-spacing:.5px}
.social{display:flex;gap:10px}
.social span{width:20px;height:20px;border-radius:50%;background:rgba(255,255,255,.85)}
.topbar svg{width:13px;height:13px;vertical-align:-2px;margin-right:6px;fill:#fff}

/* header */
.header{left:0;top:44px;width:1200px;height:98px;background:#fff}
.nav{position:absolute;left:286px;top:0;height:98px;display:flex;align-items:center;gap:38px;font-family:"Vollkorn",serif;font-size:15px;letter-spacing:1.2px;color:var(--ink)}
.nav .home svg{width:22px;height:22px;fill:var(--red)}
.nav .search svg{width:16px;height:16px;stroke:#aaa;fill:none;stroke-width:2}
.logo{left:98px;top:54px;width:146px;height:146px;border-radius:50%;background:#fff;z-index:3;display:flex;align-items:center;justify-content:center;text-align:center;font-family:"Vollkorn",serif;font-weight:700;font-size:21px;line-height:1.1;color:var(--red);box-shadow:0 2px 8px rgba(0,0,0,.15)}

/* hero */
.hero{left:0;top:142px;width:1200px;height:486px}
.hero svg{display:block}
.hero-title{left:0;top:468px;width:1200px;text-align:center;color:#fff;font-family:"Vollkorn",serif}
.hero-title .script{display:block;font-style:italic;font-size:56px;line-height:1}
.hero-title .main{display:block;font-size:42px;letter-spacing:1px;line-height:1.15}
.read-badge{left:569px;top:318px;width:62px;height:62px;border-radius:50%;background:var(--red);color:#fff;font-size:9px;font-weight:700;text-align:center;padding-top:17px;line-height:1.2;border:2px solid #fff}
.dots{left:0;top:603px;width:1200px;display:flex;justify-content:center;gap:10px}
.dots span{width:9px;height:9px;border-radius:50%;border:1px solid #fff}
.dots span:first-child{background:#fff}

/* about */
.about-collage{left:340px;top:628px;width:860px;height:602px}
.about-label{left:98px;top:728px;font-size:15px;color:var(--ink)}
.about-title{left:98px;top:758px;font-family:"Vollkorn",serif;font-weight:600;font-size:35px;line-height:1.15;color:var(--orange);text-transform:uppercase}
.about-rule{left:98px;top:868px;width:80px;height:3px;background:var(--orange)}
.about-text{left:98px;top:898px;width:400px;font-size:13px;line-height:1.6;text-align:justify}
.btn-pill{left:98px;top:1122px;width:175px;height:44px;border-radius:22px;background:var(--red);color:#fff;font-size:12px;font-weight:700;letter-spacing:.5px;display:flex;align-items:center;padding-left:28px;gap:32px}
.btn-pill svg{width:16px;height:12px;stroke:#fff;fill:none;stroke-width:2}

/* section heads */
.section-head{left:0;width:1200px;text-align:center}
.mark{display:block;margin:0 auto 12px;width:48px;height:48px;border-radius:50%;background:#fff;border:2px solid var(--red)}
.section-head h2{font-family:"Vollkorn",serif;font-weight:700;font-size:32px;letter-spacing:1px}
.section-head .rule{display:block;width:50px;height:3px;margin:12px auto 0}

/* government */
.government{left:0;top:1230px;width:1200px;height:578px;background:var(--grey-bg)}
.gov-head{top:1262px}
.gov-head h2{color:var(--red)}
.gov-head .rule{background:#222}
.gov-highlight{left:435px;top:1403px;width:330px;height:405px;background:#f8f8f8;box-shadow:0 0 10px rgba(0,0,0,.06)}
.gov-card{top:1440px;width:300px;text-align:center}
.gov-icon{width:110px;height:110px;border-radius:50%;background:#fff;margin:0 auto;display:flex;align-items:center;justify-content:center;box-shadow:0 2px 6px rgba(0,0,0,.08)}
.gov-icon svg{width:56px;height:56px;fill:#222}
.gov-card h3{margin-top:26px;font-family:"Vollkorn",serif;font-size:18px;font-weight:700;color:var(--red);text-transform:uppercase}
.gov-card p{margin:10px auto 0;width:230px;font-size:12px;line-height:1.5}
.btn-sq{display:inline-block;margin-top:20px;width:104px;height:32px;line-height:32px;background:var(--red);color:#fff;font-size:11px;font-weight:700}
.side-arrow{top:1572px;width:22px;height:56px;background:#fff;display:flex;align-items:center;justify-content:center}
.side-arrow svg{width:8px;height:14px;stroke:#999;fill:none;stroke-width:2}

/* program */
.program{left:0;top:1808px;width:1200px;height:763px;background:
  repeating-linear-gradient(90deg,rgba(0,0,0,.18) 0 3px,transparent 3px 118px),
  linear-gradient(90deg,var(--wood) 0%,var(--wood-light) 35%,var(--wood) 60%,var(--wood-light) 100%)}
.prog-head{top:1850px}
.prog-head .mark{border-color:#fff}
.prog-head h2{color:#fff}
.prog-head .rule{background:#fff}
.card{top:1999px;width:464px;height:518px;background:#fff;padding:34px 34px 0}
.card-bar{height:64px;background:var(--red);color:#fff;display:flex;align-items:center;justify-content:space-between;padding:0 20px;font-family:"Vollkorn",serif;font-size:21px}
.card-bar svg{width:10px;height:18px;stroke:#fff;fill:none;stroke-width:2}
.news-img{margin-top:29px;height:220px;background:linear-gradient(180deg,#8fb3dc 0%,#c9dbee 55%,#6c7b58 80%,#4b5a3c 100%)}
.news-title{margin-top:32px;font-family:"Vollkorn",serif;font-size:24px;color:var(--ink)}
.date{font-size:11px;color:var(--red);margin-top:6px;display:flex;align-items:center;gap:6px}
.date svg{width:11px;height:11px;fill:var(--red)}
.news-text{margin-top:10px;font-size:13px;line-height:1.5}
.event{display:flex;gap:16px;margin-top:30px;height:92px}
.event + .event{margin-top:28px}
.event-img{width:120px;height:85px;flex:none}
.event h4{font-family:"Vollkorn",serif;font-weight:400;font-size:15px;color:var(--ink)}
.event p{font-size:11px;line-height:1.5;margin-top:6px;width:230px}
.event-meta{display:flex;justify-content:space-between;font-size:11px;color:var(--red);margin-top:8px;margin-left:-136px}

/* arms-length */
.arms-title{left:60px;top:2600px;width:294px;text-align:right;font-family:"Vollkorn",serif;font-weight:700;font-size:35px;line-height:1.1;color:var(--red)}
.arms-divider{left:386px;top:2571px;width:1px;height:129px;background:var(--line)}
.arms-text{left:428px;top:2596px;width:745px;font-size:15px;line-height:1.55;color:#b5b5b5}

/* forms */
.tabs{left:98px;top:2762px;width:1002px;height:68px;display:flex}
.tab{flex:1;display:flex;align-items:center;justify-content:center;gap:12px;font-size:14px;font-weight:700;letter-spacing:.5px;background:#e3e3e3;color:#333}
.tab.active{background:var(--red);color:#fff}
.tab svg{width:18px;height:22px}
.form-panel{left:98px;top:2830px;width:1002px;height:274px;background:#fff;box-shadow:0 2px 10px rgba(0,0,0,.12);border-top:3px solid var(--red)}
.field{position:absolute;height:42px;border:1px solid #b9dcd8;background:#fff;font-size:13px;color:#888;padding:12px 14px}
.submit{position:absolute;left:506px;top:134px;width:466px;height:84px;background:linear-gradient(180deg,#d3141d,var(--red-dark));color:#fff;font-family:"Vollkorn",serif;font-size:24px;display:flex;align-items:center;justify-content:center;border-radius:3px}

/* contact */
.contact-bg{left:0;top:3140px;width:1200px;height:526px;background:linear-gradient(180deg,#fff 0%,#f3f3f3 60%,#e9e9e9 100%)}
.contact-title{left:0;top:3184px;width:1200px;text-align:center;font-family:"Raleway",sans-serif;font-size:28px;letter-spacing:1px;color:#222}
.contact-sub{left:0;top:3230px;width:1200px;text-align:center;font-size:14px;color:#666}
.contact-rule{left:98px;top:3290px;width:1002px;height:2px;background:var(--gold)}
.contact-item{top:3322px;display:flex;gap:22px}
.contact-item svg{width:48px;height:44px;stroke:var(--gold);fill:none;stroke-width:2}
.contact-item h5{font-size:12px;font-weight:700;color:var(--gold);text-transform:uppercase;letter-spacing:.5px}
.contact-item p{font-size:13px;color:#333;line-height:1.55;margin-top:4px}
.triangle{left:0;top:3370px;width:1200px;height:296px}
.footer-text{left:0;top:3582px;width:1200px;text-align:center;font-size:12px;line-height:1.8;color:#333;letter-spacing:.3px}
.to-top{left:1100px;top:3617px;width:60px;height:49px;background:#e1e1e1;display:flex;align-items:center;justify-content:center}
.to-top svg{width:14px;height:14px;stroke:#999;fill:none;stroke-width:2}
</style>
</head>
<body>

<!-- top bar -->
<div class="abs topbar">
  <span><svg viewBox="0 0 24 24"><path d="M6.6 10.8a15 15 0 0 0 6.6 6.6l2.2-2.2c.3-.3.7-.4 1-.2 1.1.4 2.3.6 3.6.6.6 0 1 .4 1 1V20c0 .6-.4 1-1 1A17 17 0 0 1 3 4c0-.6.4-1 1-1h3.5c.6 0 1 .4 1 1 0 1.3.2 2.5.6 3.6.1.3 0 .7-.2 1z"/></svg>Call us: (123) 456-7890</span>
  <span><svg viewBox="0 0 24 24"><path d="M2 5h20v14H2z M2 5l10 8 10-8" stroke="#fff" fill="none" stroke-width="2"/></svg>E-mail: info@emailaddress.com</span>
  <div class="right">
    <span><svg viewBox="0 0 24 24"><path d="M6 10V7a6 6 0 0 1 12 0v3h1v12H5V10zm2 0h8V7a4 4 0 0 0-8 0z"/></svg>Login</span>
    <span>SELECT LANGUAGE ▾</span>
    <div class="social"><span></span><span></span><span></span><span></span></div>
  </div>
</div>

<!-- header -->
<header class="abs header">
  <nav class="nav">
    <a class="home" href="#"><svg viewBox="0 0 24 24"><path d="M12 3l10 9h-3v9h-5v-6h-4v6H5v-9H2z"/></svg></a>
    <a href="#">ABOUT</a>
    <a href="#">GOVERMENT</a>
    <a href="#">PROGRAM</a>
    <a href="#">ARMS-LENGTH ENTITIES</a>
    <a href="#">I WANT TO</a>
    <a class="search" href="#"><svg viewBox="0 0 24 24"><circle cx="10" cy="10" r="7"/><path d="M15 15l6 6"/></svg></a>
  </nav>
</header>
<div class="abs logo">Tessaly<br>First<br>Nation</div>

<!-- hero -->
<section class="abs hero">
  <svg width="1200" height="486" viewBox="0 0 1200 486">
    <defs>
      <linearGradient id="heroBg" x1="0" y1="0" x2="0" y2="1"><stop offset="0" stop-color="#3a3a3a"/><stop offset="1" stop-color="#1f1f1f"/></linearGradient>
      <linearGradient id="portrait" x1="0" y1="0" x2="1" y2="1"><stop offset="0" stop-color="#9a9a9a"/><stop offset="1" stop-color="#4a4a4a"/></linearGradient>
      <radialGradient id="sunset" cx=".5" cy=".55" r=".6"><stop offset="0" stop-color="#fff3b0"/><stop offset=".35" stop-color="#f7c21b"/><stop offset="1" stop-color="#c85a0a"/></radialGradient>
    </defs>
    <rect width="1200" height="486" fill="url(#heroBg)"/>
    <polygon role="img" aria-label="Portrait of a young community member" points="342,15 552,225 342,435 132,225" fill="url(#portrait)"/>
    <polygon points="855,-30 1085,200 855,430 625,200" fill="#f5a623"/>
    <polygon role="img" aria-label="Silhouette of a woman at sunset" points="855,-14 1069,200 855,414 641,200" fill="url(#sunset)"/>
    <polygon points="600,158 850,408 600,658 350,408" fill="#fff"/>
    <polygon points="600,172 836,408 600,644 364,408" fill="#c4121b"/>
  </svg>
</section>
<div class="abs read-badge">READ<br>MORE<br>→</div>
<div class="abs hero-title"><span class="script">Tessaly</span><span class="main">FIRST NATION</span></div>
<div class="abs dots"><span></span><span></span><span></span><span></span><span></span></div>

<!-- about -->
<svg class="abs about-collage" viewBox="0 0 860 602">
  <defs>
    <linearGradient id="moccasin" x1="0" y1="0" x2="1" y2="1"><stop offset="0" stop-color="#d9a441"/><stop offset="1" stop-color="#8c5a1e"/></linearGradient>
    <linearGradient id="snow" x1="0" y1="0" x2="0" y2="1"><stop offset="0" stop-color="#b8cde3"/><stop offset="1" stop-color="#eef2f6"/></linearGradient>
    <linearGradient id="smile" x1="0" y1="0" x2="1" y2="1"><stop offset="0" stop-color="#5a88b0"/><stop offset="1" stop-color="#c98a6a"/></linearGradient>
    <radialGradient id="beads" cx=".5" cy=".5" r=".6"><stop offset="0" stop-color="#e24097"/><stop offset=".5" stop-color="#c4121b"/><stop offset="1" stop-color="#3a7d3a"/></radialGradient>
  </defs>
  <polyline points="39,3 247,210 479,3" fill="none" stroke="#f9d38a" stroke-width="12"/>
  <polygon role="img" aria-label="Beaded moccasins" points="467,57 699,289 467,521 235,289" fill="url(#moccasin)"/>
  <polygon role="img" aria-label="Two people walking in a winter forest" points="674,-29 882,179 674,387 466,179" fill="url(#snow)"/>
  <polygon points="860,200 860,430 745,315" fill="#3a3a3a"/>
  <polygon role="img" aria-label="Smiling woman outdoors" points="674,264 857,447 674,630 491,447" fill="url(#smile)"/>
  <polygon role="img" aria-label="Traditional floral beadwork" points="250,382 400,532 250,682 100,532" fill="url(#beads)"/>
  <polygon points="430,602 475,557 520,602" fill="#c4121b"/>
  <polygon points="640,602 665,577 690,602" fill="#c4121b"/>
</svg>
<div class="abs about-label">About us</div>
<h1 class="abs about-title">Welcome to<br>Tessaly First Nation</h1>
<div class="abs about-rule"></div>
<p class="abs about-text">Lorem Ipsum is simply dummy text of the printing and typesetting industry. Lorem Ipsum has been the industry's standard dummy text ever since the 1500s, when an unknown printer took a galley of type and scrambled it to make a type specimen book. It has survived not only five centuries, but also the leap into electronic typesetting, remaining essentially unchanged. It was popularised in the 1960s with the release of Letraset sheets containing Lorem Ipsum passages, and more recently with desktop publishing software like Aldus PageMaker including versions of Lorem Ipsum.</p>
<a class="abs btn-pill" href="#">READ MORE <svg viewBox="0 0 16 12"><path d="M0 6h14M9 1l5 5-5 5"/></svg></a>

<!-- government -->
<section class="abs government"></section>
<div class="abs gov-highlight"></div>
<div class="abs section-head gov-head"><span class="mark"></span><h2>GOVERNMENT</h2><span class="rule"></span></div>
<div class="abs gov-card" style="left:107px">
  <div class="gov-icon"><svg viewBox="0 0 48 48"><path d="M24 6a10 10 0 0 1 10 10H14A10 10 0 0 1 24 6zM10 18h28v3H10zM13 23h3v14h-3zm7 0h3v14h-3zm5 0h3v14h-3zm7 0h3v14h-3zM8 38h32v4H8z"/></svg></div>
  <h3>Council</h3>
  <p>Lorem Ipsum is simply dummy text of the printing and typesetting industry. Lorem Ipsum has been the industry's standard dummy text ever since the 1500s, when an unknown printer took a galley of type.</p>
  <a class="btn-sq" href="#">READ MORE</a>
</div>
<div class="abs gov-card" style="left:450px">
  <div class="gov-icon"><svg viewBox="0 0 48 48"><circle cx="24" cy="14" r="7"/><circle cx="12" cy="18" r="5"/><circle cx="36" cy="18" r="5"/><path d="M12 40c0-8 5-14 12-14s12 6 12 14zM2 36c0-6 4-10 9-10 1 0 2 0 3 .5C11 29 10 33 10 36zm44 0c0-6-4-10-9-10-1 0-2 0-3 .5 3 2.5 4 6.5 4 9.5z"/></svg></div>
  <h3>General Assembly</h3>
  <p>Lorem Ipsum is simply dummy text of the printing and typesetting industry. Lorem Ipsum has been the industry's standard dummy text ever since the 1500s, when an unknown printer took a galley of type.</p>
  <a class="btn-sq" href="#">READ MORE</a>
</div>
<div class="abs gov-card" style="left:786px">
  <div class="gov-icon"><svg viewBox="0 0 48 48"><circle cx="14" cy="12" r="4"/><circle cx="24" cy="10" r="4"/><circle cx="34" cy="12" r="4"/><path d="M8 24c0-5 3-8 6-8s6 3 6 8zm10-2c0-5 3-8 6-8s6 3 6 8zm10 2c0-5 3-8 6-8s6 3 6 8zM4 26h40v4H4zM8 30h3v10H8zm29 0h3v10h-3z"/></svg></div>
  <h3>Elders Council</h3>
  <p>Lorem Ipsum is simply dummy text of the printing and typesetting industry. Lorem Ipsum has been the industry's standard dummy text ever since the 1500s, when an unknown printer took a galley of type.</p>
  <a class="btn-sq" href="#">READ MORE</a>
</div>
<div class="abs side-arrow" style="left:0"><svg viewBox="0 0 8 14"><path d="M7 1L1 7l6 6"/></svg></div>
<div class="abs side-arrow" style="left:1178px"><svg viewBox="0 0 8 14"><path d="M1 1l6 6-6 6"/></svg></div>

<!-- program -->
<section class="abs program"></section>
<div class="abs section-head prog-head"><span class="mark"></span><h2>PROGRAM</h2><span class="rule"></span></div>
<article class="abs card" style="left:122px">
  <div class="card-bar"><svg viewBox="0 0 10 18"><path d="M9 1L1 9l8 8"/></svg>LATEST NEWS<svg viewBox="0 0 10 18"><path d="M1 1l8 8-8 8"/></svg></div>
  <div class="news-img" role="img" aria-label="Children playing on a swing under a blue sky"></div>
  <h3 class="news-title">Where does it come from?</h3>
  <div class="date"><svg viewBox="0 0 12 12"><path d="M1 2h10v9H1zM3 0h1v2H3zm5 0h1v2H8z"/></svg>February 22, 2018</div>
  <p class="news-text">Lorem Ipsum is simply dummy text of the printing and typesetting industry. Lorem Ipsum has been the industry's standard dummy text ever since the 1500s, when an unknown printer took a galley.</p>
</article>
<article class="abs card" style="left:611px">
  <div class="card-bar"><svg viewBox="0 0 10 18"><path d="M9 1L1 9l8 8"/></svg>EVENTS<svg viewBox="0 0 10 18"><path d="M1 1l8 8-8 8"/></svg></div>
  <div class="event">
    <div class="event-img" role="img" aria-label="Family standing outdoors in winter" style="background:linear-gradient(180deg,#9cc0de,#e8eef3 60%,#7b5a4a)"></div>
    <div><h4>Where can I get some ?</h4><p>Lorem Ipsum is simply dummy text of the printing and typesetting industry. Lorem Ipsum has been the industry's standard dummy text</p>
    <div class="event-meta"><span>▣ February 22, 2018</span><span>◷ 10.00-20.00</span></div></div>
  </div>
  <div class="event">
    <div class="event-img" role="img" aria-label="Portrait of a community member" style="background:linear-gradient(135deg,#b9b2a8,#6a5a52)"></div>
    <div><h4>Where can I get some ?</h4><p>Lorem Ipsum is simply dummy text of the printing and typesetting industry. Lorem Ipsum has been the industry's standard dummy text</p>
    <div class="event-meta"><span>▣ February 22, 2018</span><span>◷ 10.00-20.00</span></div></div>
  </div>
  <div class="event">
    <div class="event-img" role="img" aria-label="Wolf in a dark forest" style="background:linear-gradient(135deg,#3a3a3a,#a9a39a)"></div>
    <div><h4>Where can I get some ?</h4><p>Lorem Ipsum is simply dummy text of the printing and typesetting industry. Lorem Ipsum has been the industry's standard dummy text</p>
    <div class="event-meta"><span>▣ February 22, 2018</span><span>◷ 10.00-20.00</span></div></div>
  </div>
</article>

<!-- arms-length -->
<h2 class="abs arms-title">ARMS-LENGTH<br>ENTITIES</h2>
<div class="abs arms-divider"></div>
<p class="abs arms-text">Lorem Ipsum is simply dummy text of the printing and typesetting industry. Lorem Ipsum has been the industry's standard dummy text ever since the 1500s, when an unknown printer took a galley of type and scrambled it to make a type specimen book.</p>

<!-- forms -->
<div class="abs tabs">
  <div class="tab active"><svg viewBox="0 0 18 22" fill="none" stroke="#fff" stroke-width="1.6"><path d="M1 1h11l5 5v15H1z M4 9h10M4 13h10M4 17h7"/></svg>FORMS BY TOPIC</div>
  <div class="tab"><svg viewBox="0 0 18 22" fill="none" stroke="#333" stroke-width="1.6"><path d="M1 1h11l5 5v15H1z M4 9h10M4 13h10M4 17h7"/></svg>FORM BY DEPARTMENT</div>
</div>
<form class="abs form-panel">
  <div class="field" style="left:30px;top:22px;width:466px">First Name</div>
  <div class="field" style="left:506px;top:22px;width:466px">Last Name</div>
  <div class="field" style="left:30px;top:78px;width:466px">E-mail Address</div>
  <div class="field" style="left:506px;top:78px;width:466px">Phone Number</div>
  <div class="field" style="left:30px;top:134px;width:466px;height:84px">Message</div>
  <div class="submit">Submit Form</div>
</form>

<!-- contact -->
<section class="abs contact-bg"></section>
<svg class="abs triangle" viewBox="0 0 1200 296"><polyline points="330,296 600,26 870,296" fill="none" stroke="#f5a623" stroke-width="12"/></svg>
<h2 class="abs contact-title">QUICK CONTACT</h2>
<p class="abs contact-sub">We can give you a fast response via</p>
<div class="abs contact-rule"></div>
<div class="abs contact-item" style="left:166px">
  <svg viewBox="0 0 48 44"><path d="M3 8h42v28H3zM3 8l21 16L45 8"/></svg>
  <div><h5>Email</h5><p>info@emailaddress.com<br>info@emailaddress.com</p></div>
</div>
<div class="abs contact-item" style="left:508px">
  <svg viewBox="0 0 48 44"><rect x="14" y="2" width="20" height="40" rx="3"/><path d="M20 36h8"/></svg>
  <div><h5>Call us !</h5><p>+123 456 7890<br>+123 456 7890</p></div>
</div>
<div class="abs contact-item" style="left:802px">
  <svg viewBox="0 0 48 44"><path d="M24 42S10 26 10 16a14 14 0 0 1 28 0c0 10-14 26-14 26z"/><circle cx="24" cy="16" r="5"/></svg>
  <div><h5>Address</h5><p>123, Main Road, New City,<br>My Country 123456</p></div>
</div>
<footer class="abs footer-text">2018 © Copyright Tessaly First Nation<br>ALL RIGHTS RESERVED</footer>
<div class="abs to-top"><svg viewBox="0 0 14 14"><path d="M2 7l5-5 5 5M2 12l5-5 5 5"/></svg></div>

</body>
</html>
```